Professional law firm looking for new professional and eye-catching business card design

Law firm in need of new business card design using existing firm logo and firm colors on thick card stock. Firm colors are navy blue, cyan blue, and gray. Please use firm's logo either on the back of the card or on the front and back. I am looking for something eye-catching and resonating but also professional.

Target Market(s)

Law firm growth by attracting clients with professional, creative, and attractive business cards.

Industry/Entity Type

Legal/Law Firm

Contact Information for Business Card

Name: Derek T. Halloway, Esq., Address: 517 E. Quintley Blvd., P.O. Box 641, Fenwick Bay, ME 04999, Phone numbers: (555) 555-0187 Office, (555) 555-0142 Fax, email address: DerekH@hqlegalfx.com, website: www.HQLegalFX.com

Font styles to use
Other font styles liked:
• Font as close as possible to matching law firm logo.

Requirements
Must have
• Must have business card details and law firm logo with law firm colors.

```html
<!DOCTYPE html>
<html lang="en">
<head>
<meta charset="utf-8">
<title>Halloway Quintley, P.A. – Business Card</title>
<link rel="stylesheet" href="https://fonts.googleapis.com/css2?family=Montserrat:wght@400;500&family=Open+Sans:wght@400&display=swap">
<style>
  :root {
    --navy-light: #3f5564;
    --navy: #1b3442;
    --navy-deep: #0e2431;
    --gray: #6b6b6b;
    --cyan: #29a8dd;
    --white: #ffffff;
    --rule: #cfd6da;
  }
  * { margin: 0; padding: 0; box-sizing: border-box; }
  html, body {
    width: 1000px;
    height: 1200px;
    overflow: hidden;
    background: var(--navy-deep);
  }
  .canvas { position: relative; width: 1000px; height: 1200px; }
  .card {
    position: absolute;
    left: 0;
    width: 1000px;
    height: 600px;
    overflow: hidden;
  }
  .card-back {
    top: 0;
    background: radial-gradient(ellipse 120% 90% at 50% 0%, var(--navy-light) 0%, var(--navy) 45%, var(--navy-deep) 100%);
  }
  .card-front {
    top: 600px;
    background: linear-gradient(160deg, var(--navy-light) 0%, var(--navy) 40%, var(--navy-deep) 100%);
  }
  .card-shapes { position: absolute; inset: 0; }
  .firm-name {
    position: absolute;
    font-family: "Montserrat", sans-serif;
    font-weight: 500;
    color: var(--cyan);
    letter-spacing: 1px;
    display: flex;
    align-items: center;
    gap: 12px;
    white-space: nowrap;
  }
  .firm-name .firm-dot {
    width: 14px;
    height: 14px;
    border-radius: 50%;
    background: var(--cyan);
    flex: none;
  }
  .card-back .firm-name {
    left: 0;
    right: 0;
    top: 290px;
    justify-content: center;
    font-size: 34px;
  }
  .card-front .firm-name {
    left: 58px;
    top: 166px;
    font-size: 22px;
    gap: 10px;
  }
  .card-front .firm-name .firm-dot { width: 12px; height: 12px; }
  .holder {
    position: absolute;
    left: 555px;
    top: 155px;
    color: var(--white);
  }
  .holder-name {
    font-family: "Open Sans", sans-serif;
    font-weight: 400;
    font-size: 38px;
    line-height: 1;
  }
  .holder-title {
    font-family: "Open Sans", sans-serif;
    font-size: 17px;
    margin: 10px 0 0 18px;
  }
  .divider {
    position: absolute;
    top: 249px;
    height: 2px;
    background: var(--rule);
  }
  .divider-short { left: 561px; width: 29px; }
  .divider-long { left: 601px; width: 316px; }
  .contact-list {
    position: absolute;
    left: 558px;
    top: 290px;
    list-style: none;
    font-family: "Montserrat", sans-serif;
    font-size: 16.5px;
    line-height: 24px;
    color: var(--white);
    letter-spacing: 0.4px;
  }
  .contact-item {
    display: flex;
    align-items: flex-start;
    margin-bottom: 11px;
  }
  .contact-item svg {
    width: 28px;
    height: 28px;
    flex: none;
    margin-right: 25px;
    fill: none;
    stroke: var(--white);
    stroke-width: 1.8;
    stroke-linecap: round;
    stroke-linejoin: round;
  }
  .contact-item.email { margin-top: 2px; }
</style>
</head>
<body>
<main class="canvas">

  <section class="card card-back" aria-label="Card back">
    <div class="firm-name"><span class="firm-dot"></span>Halloway Quintley, P.A.</div>
  </section>

  <section class="card card-front" aria-label="Card front">
    <svg class="card-shapes" viewBox="0 0 1000 600" width="1000" height="600">
      <defs>
        <linearGradient id="band-tone" x1="0" y1="0" x2="1" y2="1">
          <stop offset="0" stop-color="#c3c7ca"/>
          <stop offset="0.55" stop-color="#7d8990"/>
          <stop offset="1" stop-color="#2c4250"/>
        </linearGradient>
        <linearGradient id="gray-panel" x1="0" y1="0" x2="1" y2="0">
          <stop offset="0" stop-color="#5f5f5f"/>
          <stop offset="1" stop-color="#6e6e6e"/>
        </linearGradient>
        <filter id="soft-shadow" x="-20%" y="-20%" width="140%" height="140%">
          <feDropShadow dx="6" dy="4" stdDeviation="7" flood-color="#000" flood-opacity="0.45"/>
        </filter>
      </defs>
      <path class="dot-band" role="img" aria-label="Dotted halftone band along the curved edge"
            d="M320,0 H515 C470,70 462,160 432,240 C408,300 384,335 362,390 H300 V0 Z"
            fill="url(#band-tone)"/>
      <path class="navy-wave"
            d="M320,0 H352 C435,50 482,120 472,210 C462,300 385,370 354,450 C334,510 324,560 320,600 H270 Z"
            fill="#1b3442" filter="url(#soft-shadow)"/>
      <path class="gray-panel"
            d="M0,0 H325 C400,40 455,110 445,200 C435,290 352,360 322,440 C302,500 288,550 280,600 H0 Z"
            fill="url(#gray-panel)" filter="url(#soft-shadow)"/>
    </svg>

    <div class="firm-name"><span class="firm-dot"></span>Halloway Quintley, P.A.</div>

    <div class="holder">
      <h1 class="holder-name">Derek T. Halloway</h1>
      <p class="holder-title">General Manager</p>
    </div>

    <span class="divider divider-short"></span>
    <span class="divider divider-long"></span>

    <ul class="contact-list">
      <li class="contact-item phone">
        <svg viewBox="0 0 28 28" aria-hidden="true">
          <path d="M7 4 L10.5 4 L12 9 L9.5 10.8 C11 14 13.5 16.5 16.8 18 L18.5 15.5 L23.5 17 L23.5 20.5 C23.5 22 22.3 23 21 23 C12 22.5 5 15.5 4.5 6.5 C4.5 5.2 5.5 4 7 4 Z"/>
          <path d="M16 4.5 A7.5 7.5 0 0 1 23.5 12"/>
          <path d="M16 8.5 A3.5 3.5 0 0 1 19.5 12"/>
        </svg>
        <span>(555) 555-0187 (Office)<br>(555) 555-0142 (Fax)</span>
      </li>
      <li class="contact-item email">
        <svg viewBox="0 0 28 28" aria-hidden="true">
          <rect x="2.5" y="6" width="23" height="16" rx="1"/>
          <path d="M2.5 6.5 L14 15.5 L25.5 6.5"/>
          <path d="M2.5 21.5 L11 13.5 M25.5 21.5 L17 13.5"/>
        </svg>
        <span>DerekH@hqlegalfx.com</span>
      </li>
      <li class="contact-item address">
        <svg viewBox="0 0 28 28" aria-hidden="true">
          <path d="M14 25 C14 25 6 16.5 6 11 A8 8 0 0 1 22 11 C22 16.5 14 25 14 25 Z"/>
          <circle cx="14" cy="11" r="3"/>
        </svg>
        <span>517 E. Quintley Blvd., P.O. Box 641,<br>Fenwick Bay, ME 04999</span>
      </li>
      <li class="contact-item web">
        <svg viewBox="0 0 28 28" aria-hidden="true">
          <path d="M7 3 L7 21 L11.5 17 L14.5 24 L17.5 22.7 L14.5 16 L20.5 16 Z"/>
        </svg>
        <span>www.HQLegalFX.com</span>
      </li>
    </ul>
  </section>

</main>
</body>
</html>
```